Kestrel Ledger company needs ad for trade publication

Kestrel Ledgers provides sales, content, production, technology, and promotion products and services to radio stations to help increase sales and solutions to improve operations and reduce costs. We are looking for a creative ad (sizes 720x250, 300x250, 728x180) with a halloween theme. An angle could be "Nothing Scarier than starting the new year in the RED" which in business terms is a net operating loss. OR "Take a bite out of your 2024 budget". Kestrel Ledgers CAN HELP!
We want to highlight on the ad 3 key benefits that Kestrel Ledgers can help (1) "Improve your NTR" (2) "Improve your cash flow" (3) "Improve your technology and operations"
Targeting radio stations during their 2024 budgeting process

```html
<!DOCTYPE html>
<html lang="en">
<head>
<meta charset="utf-8">
<title>Kestrel Ledgers – Halloween Budget Banners</title>
<link rel="stylesheet" href="https://fonts.googleapis.com/css2?family=Creepster&family=Roboto:wght@400;500;700&display=swap">
<style>
  :root {
    --page-bg: #9ea9f0;
    --navy: #2b3a98;
    --night: #1d2a5a;
    --hill: #16303a;
    --white: #ffffff;
    --alert-red: #e01b1b;
    --cta-gold: #f2a81d;
    --arrow-orange: #f2a81d;
    --brand-blue: #1e8fe0;
    --moon-orange: #f4a23a;
  }
  * { box-sizing: border-box; margin: 0; padding: 0; }
  html, body { width: 686px; height: 1200px; overflow: hidden; }
  body { background: var(--page-bg); font-family: "Roboto", Arial, sans-serif; position: relative; }

  .banner {
    position: absolute; overflow: hidden;
    background: var(--navy);
    box-shadow: 4px 6px 10px rgba(0,0,0,.45);
    color: var(--white);
  }
  .banner > * { position: absolute; }

  .scenery {
    inset: 0;
    background: linear-gradient(180deg, rgba(43,58,152,0) 0%, rgba(43,58,152,0) 55%, var(--night) 75%, var(--hill) 100%);
  }
  .artwork {
    right: 0; bottom: 0;
    background: radial-gradient(circle at 45% 40%, var(--moon-orange) 0%, #c97a3a 35%, rgba(43,58,152,0) 70%),
                linear-gradient(180deg, rgba(0,0,0,0) 50%, rgba(150,80,20,.55) 100%);
  }
  .brand-corner {
    top: 0; right: 0; background: var(--white);
    border-bottom-left-radius: 100% 100%;
    display: flex; align-items: center; justify-content: flex-end;
  }
  .brand-name {
    color: var(--brand-blue); font-weight: 700; text-align: center;
    line-height: 1.05; letter-spacing: .3px;
  }

  .kicker, .subline { font-weight: 500; text-transform: uppercase; line-height: 1; white-space: nowrap; }
  .headline { font-family: "Creepster", "Roboto", cursive; line-height: 1; white-space: nowrap; letter-spacing: 1px; }
  .headline.tight { letter-spacing: 0; }
  .red-tag { background: var(--alert-red); padding: 0 3px; }
  .centered { text-align: center; transform: translateX(-50%); }

  .divider { width: 1.5px; background: var(--white); }

  .helper { font-weight: 500; text-transform: uppercase; white-space: nowrap; line-height: 1; }
  .help-tag { background: var(--alert-red); font-weight: 500; padding: 1px 3px; white-space: nowrap; line-height: 1; }
  .benefits-title { font-weight: 700; text-transform: uppercase; white-space: nowrap; line-height: 1; }
  .benefit-list { list-style: none; }
  .benefit-list li { position: relative; white-space: nowrap; }
  .benefit-list li::before {
    content: ""; position: absolute; left: -0.95em; top: .2em;
    border-left: .55em solid var(--arrow-orange);
    border-top: .35em solid transparent; border-bottom: .35em solid transparent;
  }
  .benefit-list li.cont::before { display: none; }

  .cta {
    background: var(--cta-gold); color: var(--white); font-weight: 700;
    border-radius: 14px; display: flex; align-items: center; justify-content: center;
    text-transform: uppercase; white-space: nowrap;
  }
</style>
</head>
<body>

<!-- Leaderboard: Nothing Scarier -->
<section class="banner" style="left:34px;top:75px;width:617px;height:214px">
  <div class="scenery" role="img" aria-label="Night sky with bats and a haunted castle silhouette over dark hills"></div>
  <div class="artwork" role="img" aria-label="Vintage radio surrounded by jack-o'-lanterns in front of an orange moon" style="width:200px;height:170px"></div>
  <div class="brand-corner" style="width:132px;height:62px;padding-right:12px"><span class="brand-name" style="font-size:15px">KESTREL<br>LEDGERS</span></div>
  <p class="kicker" style="left:49px;top:33px;font-size:15px">Nothing</p>
  <h1 class="headline" style="left:45px;top:48px;font-size:64px">SCARIER</h1>
  <p class="subline" style="left:49px;top:120px;font-size:16px">Than starting the</p>
  <p class="subline" style="left:49px;top:141px;font-size:16px">New year in the <span class="red-tag">Red</span></p>
  <div class="divider" style="left:247px;top:51px;height:103px"></div>
  <h2 class="benefits-title" style="left:266px;top:54px;font-size:16px">Key Benefits</h2>
  <ul class="benefit-list" style="left:279px;top:76px;font-size:13px;line-height:17.5px">
    <li>Improve your NTR</li><li>Improve your cash flow</li><li>Improve your technology</li><li class="cont">and operations</li>
  </ul>
  <a class="cta" style="left:206px;top:171px;width:99px;height:24px;font-size:12px">Learn more</a>
</section>

<!-- Leaderboard: Bite Out -->
<section class="banner" style="left:34px;top:309px;width:617px;height:213px">
  <div class="scenery" role="img" aria-label="Night sky with bats and a haunted castle silhouette over dark hills"></div>
  <div class="artwork" role="img" aria-label="Retro radio with carved pumpkins and a small ghost" style="width:200px;height:170px"></div>
  <div class="brand-corner" style="width:132px;height:62px;padding-right:12px"><span class="brand-name" style="font-size:15px">KESTREL<br>LEDGERS</span></div>
  <p class="kicker centered" style="left:126px;top:40px;font-size:20px">Take a</p>
  <h1 class="headline centered" style="left:126px;top:61px;font-size:58px">BITE OUT</h1>
  <p class="subline centered" style="left:126px;top:126px;font-size:17px">Of your 2024 budget</p>
  <div class="divider" style="left:251px;top:45px;height:110px"></div>
  <p class="helper" style="left:267px;top:28px;font-size:16px">Kestrel Ledgers</p>
  <span class="help-tag" style="left:266px;top:48px;font-size:15px">CAN HELP!</span>
  <h2 class="benefits-title" style="left:266px;top:70px;font-size:16px">Key Benefits</h2>
  <ul class="benefit-list" style="left:279px;top:92px;font-size:13px;line-height:17.5px">
    <li>Improve your NTR</li><li>Improve your cash flow</li><li>Improve your technology</li><li class="cont">and operations</li>
  </ul>
  <a class="cta" style="left:206px;top:171px;width:99px;height:24px;font-size:12px">Learn more</a>
</section>

<!-- Wide: Nothing Scarier -->
<section class="banner" style="left:31px;top:540px;width:624px;height:153px">
  <div class="scenery" role="img" aria-label="Night sky with bats and a haunted castle silhouette over dark hills"></div>
  <div class="artwork" role="img" aria-label="Vintage radio surrounded by jack-o'-lanterns in front of an orange moon" style="width:140px;height:120px"></div>
  <div class="brand-corner" style="width:124px;height:60px;padding-right:12px"><span class="brand-name" style="font-size:15px">KESTREL<br>LEDGERS</span></div>
  <p class="kicker" style="left:23px;top:22px;font-size:14px">Nothing</p>
  <h1 class="headline" style="left:20px;top:34px;font-size:58px">SCARIER</h1>
  <p class="subline" style="left:23px;top:101px;font-size:15px">Than starting the</p>
  <p class="subline" style="left:23px;top:121px;font-size:15px">New year in the <span class="red-tag">Red</span></p>
  <div class="divider" style="left:202px;top:40px;height:82px"></div>
  <h2 class="benefits-title" style="left:219px;top:41px;font-size:15px">Key Benefits</h2>
  <ul class="benefit-list" style="left:231px;top:60px;font-size:12px;line-height:16px">
    <li>Improve your NTR</li><li>Improve your cash flow</li><li>Improve your technology</li><li class="cont">and operations</li>
  </ul>
  <a class="cta" style="left:381px;top:66px;width:98px;height:24px;font-size:12px">Learn more</a>
</section>

<!-- Wide: Bite Out -->
<section class="banner" style="left:31px;top:713px;width:624px;height:153px">
  <div class="scenery" role="img" aria-label="Night sky with bats and a haunted castle silhouette over dark hills"></div>
  <div class="artwork" role="img" aria-label="Retro radio with carved pumpkins and a small ghost" style="width:140px;height:120px"></div>
  <div class="brand-corner" style="width:124px;height:60px;padding-right:12px"><span class="brand-name" style="font-size:15px">KESTREL<br>LEDGERS</span></div>
  <p class="kicker centered" style="left:119px;top:33px;font-size:17px">Take a</p>
  <h1 class="headline centered" style="left:119px;top:50px;font-size:50px">BITE OUT</h1>
  <p class="subline centered" style="left:119px;top:104px;font-size:15px">Of your 2024 budget</p>
  <div class="divider" style="left:220px;top:28px;height:107px"></div>
  <p class="helper" style="left:233px;top:22px;font-size:14px">Kestrel Ledgers</p>
  <span class="help-tag" style="left:232px;top:39px;font-size:13px">CAN HELP!</span>
  <h2 class="benefits-title" style="left:232px;top:57px;font-size:14px">Key Benefits</h2>
  <ul class="benefit-list" style="left:243px;top:76px;font-size:11px;line-height:14px">
    <li>Improve your NTR</li><li>Improve your cash flow</li><li>Improve your technology</li><li class="cont">and operations</li>
  </ul>
  <a class="cta" style="left:381px;top:66px;width:98px;height:24px;font-size:12px">Learn more</a>
</section>

<!-- Square: Nothing Scarier -->
<section class="banner" style="left:34px;top:886px;width:287px;height:238px">
  <div class="scenery" role="img" aria-label="Night sky with bats and a haunted castle silhouette over dark hills"></div>
  <div class="artwork" role="img" aria-label="Vintage radio surrounded by jack-o'-lanterns in front of an orange moon" style="width:140px;height:172px"></div>
  <div class="brand-corner" style="width:133px;height:65px;padding-right:10px"><span class="brand-name" style="font-size:14px">KESTREL<br>LEDGERS</span></div>
  <p class="kicker" style="left:21px;top:12px;font-size:12px">Nothing</p>
  <h1 class="headline tight" style="left:18px;top:25px;font-size:46px">SCARIER</h1>
  <p class="subline" style="left:21px;top:80px;font-size:13px">Than starting the</p>
  <p class="subline" style="left:21px;top:98px;font-size:13px">New year in the <span class="red-tag">Red</span></p>
  <h2 class="benefits-title" style="left:21px;top:133px;font-size:13px">Key Benefits</h2>
  <ul class="benefit-list" style="left:31px;top:148px;font-size:10px;line-height:13px">
    <li>Improve your NTR</li><li>Improve your cash flow</li><li>Improve your technology</li><li class="cont">and operations</li>
  </ul>
  <a class="cta" style="left:19px;top:205px;width:99px;height:23px;font-size:12px">Learn more</a>
</section>

<!-- Square: Bite Out -->
<section class="banner" style="left:343px;top:886px;width:288px;height:238px">
  <div class="scenery" role="img" aria-label="Night sky with bats and a haunted castle silhouette over dark hills"></div>
  <div class="artwork" role="img" aria-label="Retro radio with carved pumpkins and a small ghost" style="width:140px;height:172px"></div>
  <div class="brand-corner" style="width:133px;height:65px;padding-right:10px"><span class="brand-name" style="font-size:14px">KESTREL<br>LEDGERS</span></div>
  <p class="kicker centered" style="left:91px;top:13px;font-size:14px">Take a</p>
  <h1 class="headline tight centered" style="left:89px;top:28px;font-size:35px">BITE OUT</h1>
  <p class="subline centered" style="left:91px;top:67px;font-size:12px">Of your 2024 budget</p>
  <p class="helper" style="left:20px;top:94px;font-size:12px">Kestrel Ledgers</p>
  <span class="help-tag" style="left:19px;top:109px;font-size:12px">CAN HELP!</span>
  <h2 class="benefits-title" style="left:19px;top:126px;font-size:13px">Key Benefits</h2>
  <ul class="benefit-list" style="left:30px;top:141px;font-size:10px;line-height:13px">
    <li>Improve your NTR</li><li>Improve your cash flow</li><li>Improve your technology</li><li class="cont">and operations</li>
  </ul>
  <a class="cta" style="left:19px;top:205px;width:99px;height:23px;font-size:12px">Learn more</a>
</section>

</body>
</html>
```